Motion Nest Business Cards

Can all designers please apply the following info on their designs' back-side of the business card: (please see brief file upload ('Info for backside...' - for required info, colours & layout)

SPECIALISING IN INDIVIDUAL PILATES INSTRUCTION
MATWORK – including small apparatus
and STUDIO:
VIVANTE 3 GLIDER
LADDER BARREL
COUNTOUR BARREL
FLEXI DOME
VIM STOOL
KIM-O-LAN

Business Cards for Motion Nest - applying the Motion Nest logo design selected earlier.
Note the business card requires both a front and back side. Please refer to two uploaded ppt-files for type of info required to be displayed, and rough position of where info could be. Require innovative / fresh approach to business card design and use of colour by designers now. Please refer to and use logo as uploaded - also for potential business card colour application.

Dear Designers,

Please note the additional inclusion / upload of two draft ppt-files that try to show where I want what type of information, for both the front & back sides of the required business card, plus an attempt at showing the high-level concept / idea of business info position.

As my 'drafts' obviously lack colour and any ability towards innovative card design or approach – I now rely on your vastly superior graphic design abilities to produce a really great business card for my business…

Looking forward to your submissions!

Kind regards, Merika for: Motion Nest 

Hello all Designers,

Can all designers please apply the following info on their designs' back-side of the business card: (please see / refer to the Brief and specifically the file upload ('Info for backside...' - for required info, colours & layout) - for the backside of the business card).

Info content (without colour, layout etc.):

and STUDIO:

VIVANTE 3 GLIDER

LADDER BARREL

COUNTOUR BARREL

FLEXI DOME

VIM STOOL

KIM-O-LAN

Thank you to all designers that submitted for consideration!

With regards,

Motion Nest

```html
<!DOCTYPE html>
<html lang="en">
<head>
<meta charset="utf-8">
<title>Motion Nest Business Cards</title>
<link rel="stylesheet" href="https://fonts.googleapis.com/css2?family=Lato:wght@400&family=Tinos&family=Cinzel:wght@400&family=PT+Serif:ital@1&display=swap">
<style>
  :root {
    --stage: #ece9e4;
    --card: #ffffff;
    --card-edge: #4a4a4a;
    --orange: #e05a1c;
    --orange-light: #f08a3a;
    --green: #3f6b12;
    --green-bright: #1aa64a;
    --text-dark: #3a3a3a;
  }
  * { margin: 0; padding: 0; box-sizing: border-box; }
  html, body {
    width: 949px; height: 1200px; overflow: hidden;
    background: var(--stage);
  }
  .card {
    position: absolute; left: 102px; width: 745px; height: 424px;
    background: var(--card);
    border: 1.5px solid var(--card-edge);
    border-radius: 20px;
    overflow: hidden;
  }
  .card--front { top: 71px; }
  .card--back { top: 621px; }

  .brand {
    position: absolute; left: 0; right: 0;
    display: flex; align-items: center; justify-content: center; gap: 18px;
  }
  .card--front .brand { top: 34px; }
  .card--back .brand { top: 30px; }
  .brand__dot {
    width: 64px; height: 64px; border-radius: 50%;
    background: var(--green);
  }
  .brand__name {
    font-family: 'Lato', sans-serif; font-weight: 400;
    font-size: 74px; line-height: 1; color: var(--orange);
    letter-spacing: -1px;
  }
  .tagline {
    position: absolute; left: 0; right: 0; text-align: center;
    font-family: 'Tinos', serif; font-size: 24px; color: var(--green);
    letter-spacing: 0.5px;
  }
  .card--front .tagline { top: 146px; }
  .card--back .tagline { top: 125px; }
  .tagline__sep { color: var(--orange); font-size: 16px; vertical-align: 3px; padding: 0 4px; }

  .contact {
    position: absolute; left: 34px; top: 243px; list-style: none;
    font-family: 'Cinzel', serif; font-size: 16px; color: var(--text-dark);
    line-height: 22.5px;
  }
  .contact li { display: flex; align-items: center; gap: 8px; }
  .contact li.contact__cont { padding-left: 22px; }
  .contact svg { width: 14px; height: 14px; flex: none; }

  .holder {
    position: absolute; left: 370px; width: 360px; top: 252px; text-align: center;
    font-family: 'PT Serif', serif; font-style: italic;
  }
  .holder__name { font-size: 18px; color: var(--green); }
  .holder__title { font-size: 14px; color: var(--orange); margin-top: 3px; }

  .bands { position: absolute; left: 0; bottom: 0; width: 745px; height: 48px; }

  .services {
    position: absolute; left: 48px; top: 183px; list-style: none;
    font-family: 'Cinzel', serif; font-size: 17px; color: var(--orange);
    line-height: 22.3px;
  }
  .services li::before {
    content: ""; display: inline-block; width: 6px; height: 6px; border-radius: 50%;
    background: var(--orange); margin-right: 11px; vertical-align: 3px;
  }
  .services small { font-size: 13px; }
  .web {
    position: absolute; left: 0; right: 0; top: 386px; text-align: center;
    font-family: 'Cinzel', serif; font-size: 14px; letter-spacing: 5px; color: var(--orange);
  }
</style>
</head>
<body>

<section class="card card--front" aria-label="Business card front">
  <div class="brand">
    <span class="brand__dot"></span>
    <span class="brand__name">Motion Nest</span>
  </div>
  <p class="tagline">BALANCE<span class="tagline__sep">•</span>STRENGTH<span class="tagline__sep">•</span>FLEXIBILITY</p>

  <ul class="contact">
    <li>
      <svg viewBox="0 0 14 14"><circle cx="7" cy="7" r="7" fill="var(--orange)"/><path d="M3.5 7.2 7 4l3.5 3.2V10.5h-7z" fill="#fff"/></svg>
      Studio Location:
    </li>
    <li class="contact__cont">12 Larkspur Crescent</li>
    <li class="contact__cont">Elmvale WA 6099</li>
    <li>
      <svg viewBox="0 0 14 14"><circle cx="7" cy="7" r="7" fill="var(--orange)"/><rect x="4.5" y="3" width="5" height="8" rx="1" fill="#fff"/></svg>
      040 000 1234
    </li>
    <li>
      <svg viewBox="0 0 14 14"><circle cx="7" cy="7" r="7" fill="var(--orange)"/><rect x="3.5" y="4.5" width="7" height="5" fill="#fff"/><path d="M3.5 4.5 7 7.3l3.5-2.8" stroke="var(--orange)" stroke-width="0.8" fill="none"/></svg>
      Info@motionnest.com
    </li>
    <li>
      <svg viewBox="0 0 14 14"><circle cx="7" cy="7" r="7" fill="var(--orange)"/><circle cx="7" cy="7" r="3.6" stroke="#fff" stroke-width="0.9" fill="none"/><path d="M3.4 7h7.2M7 3.4v7.2" stroke="#fff" stroke-width="0.9"/></svg>
      www.motionnest.com.au
    </li>
  </ul>

  <div class="holder">
    <p class="holder__name">Merika Tallberg</p>
    <p class="holder__title">Diploma of Professional Pilates Instruction</p>
  </div>

  <svg class="bands" viewBox="0 0 745 48" preserveAspectRatio="none">
    <defs>
      <linearGradient id="band-green" x1="0" x2="1">
        <stop offset="0" stop-color="var(--green)"/>
        <stop offset="0.5" stop-color="var(--green-bright)"/>
        <stop offset="1" stop-color="var(--green)"/>
      </linearGradient>
      <linearGradient id="band-orange" x1="0" x2="1">
        <stop offset="0" stop-color="var(--orange)"/>
        <stop offset="0.5" stop-color="var(--orange-light)"/>
        <stop offset="1" stop-color="var(--orange)"/>
      </linearGradient>
    </defs>
    <polygon points="0,22 408,22 392,48 0,48" fill="url(#band-green)"/>
    <polygon points="402,48 384,48 404,0 745,0 745,48" fill="url(#band-orange)"/>
  </svg>
</section>

<section class="card card--back" aria-label="Business card back">
  <div class="brand">
    <span class="brand__dot"></span>
    <span class="brand__name">Motion Nest</span>
  </div>
  <p class="tagline">BALANCE<span class="tagline__sep">•</span>STRENGTH<span class="tagline__sep">•</span>FLEXIBILITY</p>

  <ul class="services">
    <li>SPECIALISING IN INDIVIDUAL PILATES INSTRUCTION</li>
    <li>MATWORK – <small>INCLUDING SMALL APPARATUS AND STUDIO</small></li>
    <li>VIVANTE 3 GLIDER</li>
    <li>LADDER BARREL</li>
    <li>COUNTOUR BARREL</li>
    <li>FLEXI DOME</li>
    <li>VIM STOOL</li>
    <li>KIM-O-LAN</li>
  </ul>

  <p class="web">WWW.MOTIONNEST.COM.AU</p>
</section>

</body>
</html>
```